KVR Biz Cards

We are a property management company that manages luxury level residential estates. As such, we need a business card design that gives a high end feel. The idea at the moment is to list the services offered on the back of the card, and our company information on the front of the card.

Services for the back of the card are as follows:
Professional Property Management service, Home Hosting & Concierge Service, Holliday Home / Income Property Management

```html
<!DOCTYPE html>
<html lang="en">
<head>
<meta charset="utf-8">
<title>KVR Business Cards</title>
<link href="https://fonts.googleapis.com/css2?family=Lato:wght@400;700&family=Montserrat:wght@400;500&display=swap" rel="stylesheet">
<style>
  :root {
    --backdrop: #cbcbcb;
    --card: #020204;
    --gold: #7f6520;
    --gold-soft: #6e581c;
  }
  * { margin: 0; padding: 0; box-sizing: border-box; }
  html, body { width: 1200px; height: 846px; overflow: hidden; }
  body {
    background: var(--backdrop);
    position: relative;
    font-family: "Lato", sans-serif;
    color: var(--gold);
  }
  .card {
    position: absolute;
    left: 346px;
    width: 508px;
    height: 290px;
    background: var(--card);
  }
  .card--front { top: 114px; }
  .card--back { top: 442px; }

  .brand {
    position: absolute;
    display: flex;
    align-items: center;
    gap: 9px;
  }
  .brand__square {
    width: 13px;
    height: 13px;
    background: var(--gold);
  }
  .brand__name {
    font-family: "Lato", sans-serif;
    font-weight: 700;
    color: var(--gold);
    letter-spacing: 1px;
    line-height: 1;
  }
  .card--front .brand { left: 112px; top: 160px; }
  .card--front .brand__name { font-size: 40px; }

  .contact {
    position: absolute;
    left: 251px;
    top: 88px;
    font-size: 15px;
    line-height: 16.2px;
  }
  .contact__name { font-weight: 700; font-size: 16px; line-height: 18px; }
  .contact__address { margin-top: 11.5px; }

  .card--back .brand {
    left: 0; right: 0;
    top: 106px;
    justify-content: center;
  }
  .card--back .brand__name { font-size: 30px; }
  .company {
    position: absolute;
    left: 0; right: 0;
    top: 143px;
    text-align: center;
    font-family: "Montserrat", sans-serif;
  }
  .company__name { font-size: 15.5px; font-weight: 500; letter-spacing: 0.6px; line-height: 17px; }
  .company__tagline { font-size: 10.5px; letter-spacing: 0.5px; color: var(--gold-soft); line-height: 12px; }
  .services {
    position: absolute;
    left: 0; right: 0;
    top: 196px;
    text-align: center;
    list-style: none;
    font-size: 12.3px;
    line-height: 14.6px;
  }
</style>
</head>
<body>
  <section class="card card--front">
    <div class="brand">
      <span class="brand__square"></span>
      <span class="brand__name">KVR</span>
    </div>
    <div class="contact">
      <p class="contact__name">Name Surname</p>
      <p>Tel. +34-900-555-214</p>
      <p>www.kvrestates.com</p>
      <p class="contact__address">Calle Mar Blava 7,<br>Port Verd, 07990,<br>Mallorca, Spain</p>
    </div>
  </section>

  <section class="card card--back">
    <div class="brand">
      <span class="brand__square"></span>
      <span class="brand__name">KVR</span>
    </div>
    <div class="company">
      <p class="company__name">KEVRO MANAGEMENT</p>
      <p class="company__tagline">Devoted to Keeping Your Home at Ease</p>
    </div>
    <ul class="services">
      <li>Professional Property Management Service</li>
      <li>Home Hosting &amp; Concierge Service</li>
      <li>Holliday Home / Income Property Management</li>
    </ul>
  </section>
</body>
</html>
```